Modellprojekt in der Jugendhilfe sucht für Abschlussbroschüre ansprechendes Design
Zielgruppe
Wir sind ein Jugendhilfeträger und haben kürzlich ein dreijähriges Modellprojekt 'Kompassnetz-Lebendige Wohngruppenarbeit' (Signet 'KN_Auszeichnung' liegt anbei) beendet. Zielgruppen sind zum Einen Kinder und Jugendliche, die in Erziehungshilfe-Wohngruppen leben und zum Anderen Fach- und Führungskräfte in der Kinder- und Jugendhilfe. Über Ablauf und Schlussfolgerungen aus dem abgeschlossenen Modellprojekt soll eine 30-seitige Broschüre mit dem Titel 'Gemeinsam auf Kurs bleiben' Untertitel 'Ein Wegbuch zum Kompassnetz' Auskunft geben.
Aufgabenstellung
- Broschüre im DIN A4 - Format,
- Dummy-Text für Projektstruktur und -beteiligte,
- Formschönes und dynamisches Design,
- Platzhalter für eigene Bilder (max. 3 pro Seite),
- die 6 Einrichtungslogos in einer Reihe auf dem Deckblatt vorne (unten),
- Der Broschüreninhalt ist in der PDF 'Kurzvorstellung enthalten',
- Vorgaben zum CD im PDF 'Hauptmanual VRL',
- Das VRL-Signet, wie im Manual beschrieben,
- das ebenfalls hochgeladene Gütesiegel kommt auf das Deckblatt

```html
<!DOCTYPE html>
<html lang="de">
<head>
<meta charset="utf-8">
<title>Gemeinsam auf Kurs bleiben – Broschüre</title>
<link href="https://fonts.googleapis.com/css2?family=Fira+Sans:wght@300;400;500;600&family=Noto+Serif:wght@400&display=swap" rel="stylesheet">
<style>
:root{
  --bg:#e9e9e9;
  --paper:#ffffff;
  --board:#2f6b45;
  --board-light:#4a8a5e;
  --orange:#e8531b;
  --blue:#1c63b0;
  --text:#3a3a3a;
  --box:#dde3f1;
  --note:#eef0e2;
  --grey:#9a9a9a;
  --green:#3aa548;
  --tag:#f6c62a;
}
*{box-sizing:border-box;margin:0;padding:0}
html,body{width:1200px;height:848px;overflow:hidden;background:var(--bg)}
.page{position:absolute;background:var(--paper);overflow:hidden}
.cover{left:50px;top:190px;width:330px;height:467px}
.spread{left:410px;top:162px;width:740px;height:523px}
.fill{position:absolute;left:0;top:0}
.seal{position:absolute;border-radius:50%;background:var(--board);border:4px solid #fff;box-shadow:0 0 0 2px #333}
.cover-title{position:absolute;left:46px;top:300px;font:600 18.5px/23px "Fira Sans",sans-serif;color:var(--blue)}
.logos{position:absolute;left:46px;top:388px;width:260px;height:56px}
.logo{position:absolute;display:flex;align-items:flex-start;gap:3px;font:500 4.2px/5px "Fira Sans",sans-serif;color:#333}
.logo i{display:block;width:7px;height:7px;flex:none}
.logo-main{left:0;top:0;font-size:5.2px;line-height:6px}
.logo-main i{width:22px;height:22px;background:var(--blue)}
.logo-main b{display:block;font-weight:500;font-size:10px;line-height:11px;color:var(--blue)}
.headline{position:absolute;left:35px;top:272px;font:400 21px/24px "Fira Sans",sans-serif;color:var(--blue)}
.sub{position:absolute;left:35px;top:322px;font:400 8.5px/10px "Fira Sans",sans-serif;color:var(--blue)}
.col{position:absolute;font:400 5.1px/7.3px "Noto Serif",serif;color:var(--text)}
.col p{margin-bottom:6px}
.col h3{font:400 7px/8.5px "Noto Serif",serif;color:var(--blue);margin-bottom:8px}
.col ul{list-style:none;margin-bottom:6px}
.col li{padding-left:6px;position:relative;margin-bottom:2px}
.col li::before{content:"›";position:absolute;left:0;color:var(--blue);font-weight:bold}
.box{position:absolute;left:423px;top:275px;width:134px;height:204px;background:var(--box);border-radius:6px;padding:14px 8px 0 10px;font:600 4.8px/7px "Fira Sans",sans-serif;color:#2a2a2a}
.box li{list-style:none;position:relative;padding-left:6px;margin-bottom:9px}
.box li::before{content:"›";position:absolute;left:0;top:-1px;color:var(--blue);font-size:7px}
.note{position:absolute;left:556px;top:16px;width:124px;height:166px;background:var(--note);transform:rotate(-2deg);box-shadow:1px 2px 3px rgba(0,0,0,.25);padding:22px 8px 0 8px;font:400 5px/6.5px "Fira Sans",sans-serif;color:#333}
.note .legend{display:flex;gap:6px;font-size:4px;margin-top:4px}
.note .legend span::before{content:"";display:inline-block;width:4px;height:4px;margin-right:2px;background:var(--c)}
.note .src{font-size:3.8px;line-height:5px;margin-top:4px}
.folio{position:absolute;top:500px;font:400 4.2px/5px "Fira Sans",sans-serif;color:#8a8a8a}
.folio b{color:var(--blue);font-weight:400}
.placeholder{position:absolute}
</style>
</head>
<body>

<section class="page cover" aria-label="Deckblatt">
  <svg class="fill" width="330" height="280" viewBox="0 0 330 280" aria-hidden="true">
    <defs><linearGradient id="boardA" x1="0" y1="0" x2="1" y2="1"><stop offset="0" stop-color="#2a6340"/><stop offset=".5" stop-color="#3f7f55"/><stop offset="1" stop-color="#2c6742"/></linearGradient></defs>
    <path d="M0 0H330V215Q160 238 0 264Z" fill="url(#boardA)"/>
    <path d="M0 264Q160 238 330 215" fill="none" stroke="var(--orange)" stroke-width="5"/>
  </svg>
  <div class="placeholder" role="img" aria-label="Kreidezeichnung auf der Tafel: Pfeile in alle Richtungen um ein gelbes Fragezeichen" style="left:0;top:0;width:330px;height:215px"></div>
  <div class="seal" style="left:22px;top:220px;width:64px;height:64px" role="img" aria-label="Platz für das Siegel"></div>
  <h1 class="cover-title">Gemeinsam auf Kurs bleiben –<br>Wege zum Kompassnetz</h1>
  <div class="logos">
    <div class="logo logo-main"><i></i><span><b>VRL</b>Gruppe Verbund<br>Regionaler Lebenshilfe</span></div>
    <div class="logo" style="left:84px;top:2px"><i style="background:var(--orange)"></i><span>Arbeitsgemeinschaft<br>Nordufer</span></div>
    <div class="logo" style="left:146px;top:2px"><i style="background:var(--orange)"></i><span>Jugendhilfe<br>Eiderland</span></div>
    <div class="logo" style="left:208px;top:2px"><i style="background:var(--orange)"></i><span>Jugendhilfe<br>Schleiblick</span></div>
    <div class="logo" style="left:84px;top:30px"><i style="background:var(--blue)"></i><span>Kinderhäuser<br>am Seeberg</span></div>
    <div class="logo" style="left:146px;top:30px"><i style="background:var(--orange)"></i><span>Pädagogische Hilfen<br>Marschgrund</span></div>
    <div class="logo" style="left:208px;top:30px"><i style="background:var(--orange)"></i><span>Sozialpädagogische<br>Hilfen Tannwald</span></div>
  </div>
</section>

<section class="page spread" aria-label="Innenseiten 4 und 5">
  <svg class="fill" width="370" height="220" viewBox="0 0 370 220" aria-hidden="true">
    <defs><linearGradient id="boardB" x1="0" y1="0" x2="1" y2="1"><stop offset="0" stop-color="#2a6340"/><stop offset=".6" stop-color="#3c7b52"/><stop offset="1" stop-color="#2c6742"/></linearGradient></defs>
    <path d="M0 0H370V162Q190 186 0 213Z" fill="url(#boardB)"/>
    <path d="M0 213Q190 186 370 162" fill="none" stroke="var(--orange)" stroke-width="5"/>
  </svg>
  <div class="placeholder" role="img" aria-label="Kreidezeichnung auf der Tafel: gestrichelte Flugbahn eines Papierfliegers" style="left:0;top:0;width:370px;height:162px"></div>
  <div class="seal" style="left:24px;top:168px;width:78px;height:78px" role="img" aria-label="Platz für das Siegel"></div>

  <h2 class="headline">Gemeinsam auf Kurs bleiben –<br>eine partizipative Lernreise</h2>
  <p class="sub">Blindtext steht hier als Platzhalter</p>

  <div class="placeholder" role="img" aria-label="Foto eines Kompasses" style="left:-6px;top:372px;width:88px;height:86px;border-radius:50%;background:radial-gradient(circle at 45% 40%,#f2f2f2,#9aa0a4)"></div>

  <div class="col" style="left:35px;top:352px;width:132px">
    <h3>Wie Beteiligung im Alltag beginnt</h3>
    <p style="padding-left:40px">Kinder und Jugendliche bringen ihre Sicht ein, wenn Regeln, Räume und Abläufe in der Wohngruppe gemeinsam besprochen werden. Wer mitredet, übernimmt auch Verantwortung für das Ergebnis.</p>
    <p style="padding-left:30px">Im ersten Projektjahr haben die Gruppen eigene Runden gegründet und erste Vereinbarungen getroffen, die bis heute gelten und weiterentwickelt werden.</p>
  </div>
  <div class="col" style="left:181px;top:366px;width:133px">
    <p>Die Fachkräfte begleiteten diesen Prozess mit offenen Fragen und viel Geduld. So entstanden Formate, die zu den Gruppen passen.</p>
    <ul>
      <li>Gruppenabende finden regelmäßig statt und werden von den Jugendlichen selbst moderiert.</li>
      <li>Beschwerdewege sind bekannt, einfach erreichbar und werden ernst genommen.</li>
    </ul>
    <p>Am Ende jeder Etappe steht eine kurze Auswertung, in der alle Beteiligten sagen, was gut lief und was sich ändern soll.</p>
  </div>

  <div class="col" style="left:423px;top:48px;width:120px">
    <p>ohne dass jemand übergangen wird. Die Gruppe entscheidet gemeinsam, welche Themen zuerst bearbeitet werden und wer dabei welche Aufgabe übernimmt.</p>
    <h3 style="font-size:6.4px;line-height:8px;margin-bottom:6px">Wie bleiben alle Stimmen im Gespräch hörbar?</h3>
    <p>Gerade jüngere Kinder brauchen Zeit und Bilder, um ihre Wünsche auszudrücken. Deshalb wurden Karten, Symbole und kurze Abstimmungen eingesetzt. Die Erfahrungen zeigen, dass kleine Schritte oft mehr bewirken als große Pläne. Wichtig ist, dass Zusagen eingehalten werden und Ergebnisse sichtbar bleiben.</p>
    <p>Jede Wohngruppe hat dafür eine Wand, an der Beschlüsse und offene Fragen hängen.</p>
  </div>

  <ul class="box">
    <li>Beteiligung braucht feste Zeiten und verlässliche Ansprechpersonen im Alltag.</li>
    <li>Kinder wissen, welche Rechte sie haben und an wen sie sich wenden können, wenn etwas nicht stimmt.</li>
    <li>Entscheidungen werden erklärt, auch wenn sie nicht allen gefallen.</li>
    <li>Fachkräfte reflektieren regelmäßig, wo sie Macht abgeben können und wo nicht.</li>
  </ul>
  <div class="placeholder" role="img" aria-label="Gelber Kofferanhänger mit handgeschriebenem Hinweis" style="left:411px;top:446px;width:98px;height:48px;background:var(--tag);border-radius:6px;transform:rotate(-12deg)"></div>

  <div class="note">
    <div>Beteiligung der Gruppen im Jahresvergleich</div>
    <svg width="108" height="76" viewBox="0 0 108 76" aria-label="Ringdiagramm">
      <g transform="rotate(-90 54 40)" fill="none" stroke-width="7">
        <circle cx="54" cy="40" r="26" stroke="#c9c9c9" stroke-dasharray="163.4 163.4"/>
        <circle cx="54" cy="40" r="26" stroke="var(--green)" stroke-dasharray="19.6 163.4"/>
        <circle cx="54" cy="40" r="26" stroke="#8f8f8f" stroke-dasharray="52.3 163.4" stroke-dashoffset="-111.1"/>
      </g>
      <text x="82" y="14" font-size="5" font-family="Fira Sans,sans-serif">12 %</text>
      <text x="8" y="22" font-size="5" font-family="Fira Sans,sans-serif">32 %</text>
      <text x="88" y="38" font-size="5" font-family="Fira Sans,sans-serif">76 %</text>
    </svg>
    <div class="legend"><span style="--c:var(--green)">Runden</span><span style="--c:#c9c9c9">Beschwerden</span><span style="--c:#8f8f8f">Projekte</span></div>
    <div class="src">Quelle: Befragung der Wohngruppen, drittes Projektjahr</div>
  </div>

  <div class="col" style="left:571px;top:203px;width:150px">
    <p>Die Rückmeldungen der Jugendlichen waren deutlich: Sie wollen mitentscheiden, wenn es um ihren Alltag geht, und sie wollen wissen, was aus ihren Ideen wird.</p>
  </div>
  <div class="placeholder" role="img" aria-label="Foto: Jugendliche sitzen lachend zusammen am Tisch" style="left:571px;top:250px;width:150px;height:112px;background:linear-gradient(135deg,#8a9bb0,#c7a58f 55%,#6d7f95)"></div>
  <div class="col" style="left:571px;top:372px;width:150px">
    <p>Im Austausch mit anderen Gruppen entstanden neue Ideen. Jugendliche besuchten sich gegenseitig, stellten ihre Runden vor und nahmen Anregungen mit nach Hause. Daraus wuchs ein Netz, das über das Projektende hinaus trägt und weiterhin gepflegt wird. Die Fachkräfte treffen sich zweimal im Jahr zum Austausch.</p>
  </div>

  <div class="folio" style="left:35px"><b>4 |</b> &nbsp; Gemeinsam auf Kurs bleiben · Ein Wegbuch zum Kompassnetz</div>
  <div class="folio" style="right:18px">Gemeinsam auf Kurs bleiben · Ein Wegbuch zum Kompassnetz &nbsp; <b>| 5</b></div>
</section>

</body>
</html>
```